Havenmark Electrical Business Card

create a simple but clear business card and letterhead - needs to be professional not too fancy and direct.

Target Market(s)

Home builders

Contact Information for Business Card

Information needed
Havenmark Electrical Contracting
EC. No. 418237
Derek Hollowell
Mobile 0437215609
derek@havenmarkelectrical.com.au

Requirements
Must have
• logo
• Havenmark Electrical Contracting - H.E.C.
• EC. No. 418237
• Derek Hollowell
• Mobile 0437215609
• derek@havenmarkelectrical.com.au
Nice to have
• black with white printing simple but clear
Should not have
• too much information
• no fancy writing

```html
<!DOCTYPE html>
<html lang="en">
<head>
<meta charset="utf-8">
<title>Havenmark Electrical Contracting – Business Card</title>
<link rel="stylesheet" href="https://fonts.googleapis.com/css2?family=Open+Sans:wght@400;700&display=swap">
<style>
  :root {
    --backdrop: #2b2b2b;
    --card-dark: #000000;
    --card-light: #ffffff;
    --ink-light: #ffffff;
    --ink-dark: #111111;
    --faint-on-dark: #121212;
    --faint-on-light: #d2d2d2;
  }
  * { margin: 0; padding: 0; box-sizing: border-box; }
  html, body {
    width: 1189px; height: 1200px; overflow: hidden;
    background: var(--backdrop);
    font-family: "Open Sans", Arial, sans-serif;
  }
  .canvas { position: relative; width: 1189px; height: 1200px; }
  .card {
    position: absolute; left: 171px; width: 857px; height: 489px;
    overflow: hidden;
  }
  .card--front { top: 68px; background: var(--card-dark); color: var(--ink-light); }
  .card--back { top: 626px; background: var(--card-light); color: var(--ink-dark); }

  .brand-backdrop { position: absolute; border-radius: 50%; }
  .card--front .brand-backdrop { left: 238px; top: 39px; width: 472px; height: 472px; background: var(--faint-on-dark); }
  .card--back .brand-backdrop { left: 523px; top: 158px; width: 342px; height: 342px; background: var(--faint-on-light); }

  .brand-mark { position: absolute; border-radius: 50%; }
  .card--front .brand-mark { left: 150px; top: 195px; width: 124px; height: 124px; background: var(--ink-light); }
  .card--back .brand-mark { left: 47px; top: 37px; width: 160px; height: 160px; background: var(--ink-dark); }

  .brand-name { position: absolute; font-weight: 700; line-height: 1; }
  .brand-name__main { display: block; letter-spacing: 1px; }
  .brand-name__sub { display: block; }
  .card--front .brand-name { left: 327px; top: 232px; }
  .card--front .brand-name__main { font-size: 40px; }
  .card--front .brand-name__sub { font-size: 22px; margin-top: 10px; }
  .card--back .brand-name { left: 225px; top: 108px; }
  .card--back .brand-name__main { font-size: 40px; }
  .card--back .brand-name__sub { font-size: 22px; margin-top: 10px; }

  .contact { position: absolute; left: 41px; top: 282px; }
  .contact__person { font-size: 29px; font-weight: 700; margin-bottom: 14px; }
  .contact__line { font-size: 20px; line-height: 34px; }
  .contact__label { font-weight: 700; }
  .contact__licence { font-size: 20px; margin-top: 8px; }
</style>
</head>
<body>
<main class="canvas">
  <section class="card card--front" aria-label="Card front">
    <div class="brand-backdrop" aria-hidden="true"></div>
    <div class="brand-mark" aria-hidden="true"></div>
    <h1 class="brand-name">
      <span class="brand-name__main">HAVENMARK</span>
      <span class="brand-name__sub">Electrical Contracting</span>
    </h1>
  </section>

  <section class="card card--back" aria-label="Card back">
    <div class="brand-backdrop" aria-hidden="true"></div>
    <div class="brand-mark" aria-hidden="true"></div>
    <h2 class="brand-name">
      <span class="brand-name__main">HAVENMARK</span>
      <span class="brand-name__sub">Electrical Contracting</span>
    </h2>
    <div class="contact">
      <p class="contact__person">Derek Hollowell</p>
      <p class="contact__line"><span class="contact__label">Mobile:</span> 0437215609</p>
      <p class="contact__line"><span class="contact__label">Email:</span> derek@havenmarkelectrical.com.au</p>
      <p class="contact__licence">EC. No. 418237</p>
    </div>
  </section>
</main>
</body>
</html>
```